Photographer's price list

I am a photographer who runs a studio (Ferngate Creative) and need to have a document to send clients detailing my packages (collections) and prices. I have written the text in a word document and need a designer to lay it out for me using my logo and two specific fonts: DejaVu Sans and LainieDaySH.

The look should be clean and modern and keep in the same style as my logo. I will primarily be using the final product as a PDF file to email to potential clients. It should stay black and white.

I would also like to be able to update the text myself as my prices and packages change. So I would like a PSD file.

I think I would like for the document to be in landscape format with "Collections" on one side and A la Carte on the other, but I am open to other ideas.

As for sizing, it should be a standard size so that clients can print it out if they like.

Requirements
Must have
• my logo
fonts: DejaVu and LainieDaySH
Easy to email
Easy to display on one page upon opening
Standard size so that printing from a home computer is easy to do.

```html
<!DOCTYPE html>
<html lang="en">
<head>
<meta charset="utf-8">
<title>Ferngate Creative – Photography Collections 2013</title>
<link rel="stylesheet" href="https://fonts.googleapis.com/css2?family=Allura&family=Noto+Sans:ital,wght@0,300;0,400;0,700;1,400;1,700&display=swap">
<style>
  :root {
    --backdrop: #8c8c8c;
    --paper: #fbfbfb;
    --box: #dcdcdc;
    --tag: #3c3c3c;
    --ink: #2a2a2a;
    --ink-soft: #7a7a7a;
    --ink-muted: #8a8a8a;
    --brand: #444444;
    --photo-light: #d9d9d9;
    --photo-mid: #a8a8a8;
    --photo-dark: #6e6e6e;
  }
  * { box-sizing: border-box; margin: 0; padding: 0; }
  html, body { width: 1200px; height: 900px; overflow: hidden; }
  body {
    background: var(--backdrop);
    font-family: "Noto Sans", "DejaVu Sans", sans-serif;
    color: var(--ink);
    position: relative;
  }
  .abs { position: absolute; }
  .script { font-family: "Allura", cursive; font-weight: 400; color: var(--ink); }

  /* ---------- spreads ---------- */
  .page { position: absolute; }
  .page--pricing { left: 75px; top: 38px; width: 532px; height: 397px; background: var(--paper); }
  .page--cover { left: 790px; top: 38px; width: 175px; height: 397px; background: #f2f2f2; }
  .page--included { left: 78px; top: 470px; width: 531px; height: 388px;
    background: linear-gradient(90deg, #e6e6e6, #d8d8d8 85%, #c6c6c6); }
  .page--collections { left: 609px; top: 470px; width: 531px; height: 388px;
    background: linear-gradient(90deg, #c4c4c4, #dadada 15%, #e2e2e2); }

  .photo { position: absolute; }
  .photo--warm { background: radial-gradient(ellipse at 45% 45%, var(--photo-light), var(--photo-mid) 70%, var(--photo-dark)); }
  .photo--bright { background: radial-gradient(ellipse at 50% 50%, #f2f2f2, var(--photo-light) 60%, var(--photo-mid)); }

  /* ---------- à la carte ---------- */
  .pricing-title { left: 92px; top: 58px; font-size: 22px; font-weight: 300; letter-spacing: 1.5px; }
  .pricing-intro { left: 92px; top: 87px; width: 490px; font-size: 10px; line-height: 1.25; }
  .item-name { font-size: 20px; white-space: nowrap; }
  .item-name--right { text-align: right; }
  .item-box { position: absolute; background: var(--box); font-size: 8.5px; line-height: 1.3;
    padding: 6px 38px 6px 10px; color: #444; }
  .item-box b { font-style: italic; color: var(--ink); }
  .item-box .note { color: var(--ink-muted); }
  .tag { position: absolute; right: 0; top: 0; bottom: 0; width: 30px; background: var(--tag); color: #fff;
    display: flex; align-items: center; justify-content: center; }
  .tag span { transform: rotate(-90deg); white-space: nowrap; font-family: "Allura", cursive; font-size: 22px; }

  /* ---------- cover ---------- */
  .cover-year { left: 790px; top: 82px; width: 175px; text-align: center; font-size: 56px; }
  .cover-name { left: 790px; top: 222px; width: 175px; text-align: center; font-size: 13px;
    letter-spacing: 1px; color: var(--brand); white-space: nowrap; }
  .cover-sub { left: 790px; top: 328px; width: 175px; text-align: center; font-size: 28px; line-height: 1.15; }

  /* ---------- collections ---------- */
  .included-title { left: 112px; top: 498px; font-size: 28px; }
  .included-list { left: 115px; top: 537px; width: 462px; font-size: 10.5px; line-height: 1.4; color: var(--ink-soft); }
  .included-list p { margin-bottom: 9px; }

  .stack { position: absolute; }
  .stack .sheet { position: absolute; inset: 0; background: #fff; border: 1px solid #bdbdbd; }
  .stack .sheet--a { transform: rotate(-4deg) translate(-4px, 6px); }
  .stack .sheet--b { transform: rotate(-2deg) translate(-2px, 3px); }
  .stack .frame { position: absolute; inset: 0; background: #fff; border: 1px solid #bdbdbd; padding: 6px;
    box-shadow: 0 1px 3px rgba(0,0,0,.25); }
  .stack .frame .photo { position: absolute; left: 6px; top: 6px; right: 6px; bottom: 6px; }
  .stack .tag { top: 6px; bottom: 6px; right: 6px; width: 32px; }
  .stack .tag--left { right: auto; left: 6px; }
  .stack .tag span { font-size: 27px; }

  .collection-title { font-size: 26px; white-space: nowrap; }
  .collection-text { font-size: 9px; line-height: 1.25; color: var(--ink); }
  .collection-text .extra { color: var(--ink-soft); font-style: italic; display: block; }
</style>
</head>
<body>

<!-- =========== Spread: à la carte + cover =========== -->
<section class="page page--pricing" aria-label="A la carte pricing"></section>

<h1 class="abs pricing-title">a la carte &nbsp;pricing</h1>
<p class="abs pricing-intro">These products may be purchased separately to complement your collection. &nbsp;A consultation with Mara will help you decide which products are best for gifts and for your home.</p>

<h2 class="abs script item-name" style="left:86px;top:122px;">high resolution digital images</h2>
<div class="item-box" style="left:86px;top:150px;width:252px;height:37px;padding-top:7px;">Perfect if you just need to add “one more image” to your collection! High-resolution jpeg file.
  <div class="tag"><span>25€</span></div></div>

<h2 class="abs script item-name" style="left:86px;top:192px;">matt prints</h2>
<div class="item-box" style="left:86px;top:215px;width:252px;height:53px;"><b>20x30 cm and smaller.</b> Each print is professionally edited, printed on archival photo paper. <span class="note">Purchase includes the JPEG file for your personal digital use.</span>
  <div class="tag"><span>25€</span></div></div>

<h2 class="abs script item-name" style="left:86px;top:286px;">brennmoor prints</h2>
<div class="item-box" style="left:86px;top:312px;width:252px;height:48px;"><b>30x40 cm.</b> Prints on Brennmoor (watercolor) paper are Mara's favorite for large format color prints.
  <div class="tag"><span>45€</span></div></div>

<h2 class="abs script item-name item-name--right" style="left:348px;top:118px;width:240px;">canvas prints</h2>
<div class="item-box" style="left:348px;top:148px;width:244px;height:57px;padding-top:18px;"><b>30x40 cm.</b> Ready-to-hang, stretched canvas wall art of your favorite images.
  <div class="tag"><span>100€</span></div></div>

<h2 class="abs script item-name item-name--right" style="left:348px;top:205px;width:240px;">framed + matted prints</h2>
<div class="item-box" style="left:348px;top:235px;width:244px;height:58px;padding-top:12px;"><b>30x40 inch.</b> Beautiful Brennmoor prints finished with wide mats and simple, elegant frames of your choice
  <div class="tag"><span>350€</span></div></div>

<h2 class="abs script item-name item-name--right" style="left:348px;top:295px;width:240px;">custom designed albums</h2>
<div class="item-box" style="left:348px;top:325px;width:244px;height:90px;padding-top:10px;">Images from your session are selected for the custom design of an album and bound in a book for a modern presentation of your images. There are a number of cover choices for the classic flush-mount and beautifully crafted albums.
  <div class="tag"><span>100€+</span></div></div>

<div class="photo photo--warm" role="img" aria-label="Black and white photo of a father holding his newborn baby" style="left:607px;top:38px;width:183px;height:287px;"></div>
<div class="photo photo--warm" role="img" aria-label="Black and white family portrait with parents, children and a newborn" style="left:607px;top:328px;width:183px;height:107px;"></div>

<section class="page page--cover" aria-label="Cover"></section>
<div class="abs script cover-year">2013</div>
<div class="abs cover-name">Ferngate Creative</div>
<div class="abs script cover-sub">photography<br>collections</div>

<div class="photo photo--bright" role="img" aria-label="Black and white photo of a family lying together on a bed" style="left:965px;top:38px;width:175px;height:117px;"></div>
<div class="photo photo--bright" role="img" aria-label="Black and white close-up photo of a baby" style="left:965px;top:160px;width:175px;height:265px;"></div>

<!-- =========== Spread: collections =========== -->
<section class="page page--included" aria-label="What all collections include"></section>
<section class="page page--collections" aria-label="Collections"></section>

<h2 class="abs script included-title">All collections include:</h2>
<div class="abs included-list">
  <p>One to two hour portrait session with photographer in location of your choice (unlimited time if necessary!)</p>
  <p>Mara will create a presentation video with hand-selected music and custom editing, which tells your story, highlights the best images, and reveals the connections within your family.</p>
  <p>An online gallery for viewing and ordering helps you share your images with family and friends.</p>
</div>

<!-- Collection 1 -->
<div class="stack" style="left:126px;top:682px;width:138px;height:96px;">
  <div class="sheet sheet--a"></div><div class="sheet sheet--b"></div>
  <div class="frame">
    <div class="photo photo--bright" role="img" aria-label="Black and white photo of a sleeping baby"></div>
    <div class="tag"><span>300€</span></div>
  </div>
</div>
<h3 class="abs script collection-title" style="left:284px;top:688px;">Collection 1</h3>
<p class="abs collection-text" style="left:284px;top:720px;width:310px;">Your favorite <b><i>five</i></b> images from the session will be professionally edited and presented to you on disk as high resolution jpegs</p>

<!-- Collection 2 -->
<div class="stack" style="left:634px;top:496px;width:134px;height:92px;">
  <div class="sheet sheet--a"></div><div class="sheet sheet--b"></div>
  <div class="frame">
    <div class="photo photo--warm" role="img" aria-label="Black and white photo of a mother and baby"></div>
    <div class="tag"><span>400€</span></div>
  </div>
</div>
<h3 class="abs script collection-title" style="left:796px;top:500px;">Collection 2</h3>
<p class="abs collection-text" style="left:796px;top:531px;width:300px;">Your favorite <b><i>ten</i></b> images from the session will be professionally edited and given to you on disk as high resolution jpegs.
  <span class="extra">Your favorite image from the session will be professionally printed for you (20x30cm) on Brennmoor paper, Mara's favorite for portraits.</span></p>

<!-- Collection 3 -->
<h3 class="abs script collection-title" style="left:637px;top:622px;">Collection 3</h3>
<p class="abs collection-text" style="left:637px;top:655px;width:295px;">Your favorite <b><i>fifteen</i></b> images from the session will be professionally edited and presented to you on disk as high resolution jpegs.
  <span class="extra">Your favorite <b>two</b> images from the session will be professionally printed for you (20x30cm) on Brennmoor paper, Mara's favorite for portraits.</span></p>
<div class="stack" style="left:946px;top:618px;width:142px;height:94px;">
  <div class="sheet sheet--a"></div><div class="sheet sheet--b"></div>
  <div class="frame">
    <div class="photo photo--warm" role="img" aria-label="Black and white portrait of a father, mother and child"></div>
    <div class="tag tag--left"><span>500€</span></div>
  </div>
</div>

<!-- Collection 4 -->
<div class="stack" style="left:638px;top:738px;width:132px;height:90px;">
  <div class="sheet sheet--a"></div><div class="sheet sheet--b"></div>
  <div class="frame">
    <div class="photo photo--bright" role="img" aria-label="Black and white photo of a family of four in a bright room"></div>
    <div class="tag"><span>600€</span></div>
  </div>
</div>
<h3 class="abs script collection-title" style="left:796px;top:736px;">Collection 4</h3>
<p class="abs collection-text" style="left:796px;top:768px;width:305px;"><b><i>ALL</i></b> presented images from the session will be professionally edited and presented to you on disk as high resolution jpegs (approx 40+ images)
  <span class="extra">Your favorite <b>two</b> images from the session will be professionally printed for you (20x30cm) on Brennmoor paper, Mara's favorite for portraits.</span></p>

</body>
</html>
```